Business card design needed

OH&S consultancy and training

Industry/Entity Type

Training

Contact Information for Business Card

Coastal Hazard & Learning Bureau
Dorian Whitfield
Director

0427 391 806
dorian.whitfield@chlbureau.com.au
chlbureau.com.au

Ph: 03 9172 4053
Fx: 03 9172 4055

```html
<!DOCTYPE html>
<html lang="en">
<head>
<meta charset="utf-8">
<title>Coastal Hazard &amp; Learning Bureau — Business Card</title>
<link rel="stylesheet" href="https://fonts.googleapis.com/css2?family=Arimo:wght@400&family=Cinzel:wght@400&display=swap">
<style>
  :root {
    --page: #ffffff;
    --card-grey: #e6e6e6;
    --card-grey-light: #f2f2f2;
    --blue-dark: #0a1f78;
    --blue-mid: #153a9e;
    --blue-light: #2456c4;
    --shadow-grey: #b4b4b4;
    --ink: #111111;
    --logo-grey: #6b6b6b;
    --accent-yellow: #f2ea00;
    --web-yellow: #f5e800;
    --white: #ffffff;
  }
  * { margin: 0; padding: 0; box-sizing: border-box; }
  html, body {
    width: 1200px; height: 900px; overflow: hidden;
    background: var(--page);
  }
  .canvas { position: relative; width: 1200px; height: 900px; }
  .card {
    position: absolute; left: 36px; top: 126px;
    width: 1128px; height: 638px; overflow: hidden;
    background: var(--card-grey);
  }
  .card-art { position: absolute; inset: 0; width: 100%; height: 100%; }
  .brand {
    position: absolute; right: 54px; top: 48px;
    display: flex; align-items: center; gap: 14px;
    font-family: "Arimo", Arial, sans-serif; color: var(--logo-grey);
  }
  .brand-mark { width: 46px; height: 46px; background: var(--accent-yellow); }
  .brand-text { display: flex; flex-direction: column; align-items: flex-end; }
  .brand-name { font-size: 48px; line-height: 1; letter-spacing: 1px; }
  .brand-tagline { font-size: 15px; margin-top: 4px; }
  .person {
    position: absolute; left: 370px; top: 338px; width: 580px;
    text-align: center; font-family: "Cinzel", "Times New Roman", serif; color: var(--ink);
  }
  .person-name { font-size: 36px; line-height: 44px; letter-spacing: 1px; }
  .person-rule { height: 1px; background: #555; margin: 2px 0 4px; }
  .person-role { font-size: 24px; line-height: 28px; text-transform: lowercase; font-variant: small-caps; letter-spacing: 2px; }
  .office-contact {
    position: absolute; left: 104px; top: 512px;
    font-family: "Arimo", Arial, sans-serif; font-size: 25px; line-height: 30px; color: var(--ink);
  }
  .mobile-contact {
    position: absolute; right: 54px; top: 534px; text-align: right;
    font-family: "Arimo", Arial, sans-serif; font-size: 25px; line-height: 26px;
  }
  .mobile { color: var(--white); }
  .website { color: var(--web-yellow); }
</style>
</head>
<body>
<main class="canvas">
  <section class="card">
    <svg class="card-art" viewBox="0 0 1128 638" preserveAspectRatio="none">
      <defs>
        <linearGradient id="bandBlue" x1="0" y1="0" x2="1" y2="0.3">
          <stop offset="0" stop-color="var(--blue-light)"/>
          <stop offset="0.5" stop-color="var(--blue-mid)"/>
          <stop offset="1" stop-color="var(--blue-dark)"/>
        </linearGradient>
        <linearGradient id="cornerBlue" x1="0" y1="1" x2="1" y2="0">
          <stop offset="0" stop-color="var(--blue-dark)"/>
          <stop offset="1" stop-color="var(--blue-light)"/>
        </linearGradient>
        <radialGradient id="fieldGrey" cx="0.5" cy="0.6" r="0.7">
          <stop offset="0" stop-color="var(--card-grey-light)"/>
          <stop offset="1" stop-color="var(--card-grey)"/>
        </radialGradient>
      </defs>
      <rect class="card-field" role="img" aria-label="Light grey dotted diamond background pattern" width="1128" height="638" fill="url(#fieldGrey)"/>
      <path class="band-shadow" fill="var(--shadow-grey)"
        d="M1128,316 C980,260 740,232 540,250 C320,270 140,400 66,638 L44,638 C120,390 300,258 520,240 C720,224 960,250 1128,304 Z"/>
      <path class="band-main" fill="url(#bandBlue)"
        d="M0,134 C180,96 380,84 560,112 C780,148 980,230 1128,304 C960,250 720,224 520,240 C300,258 120,390 44,638 L0,638 Z"/>
      <path class="corner-wedge" fill="url(#cornerBlue)"
        d="M714,638 C840,566 980,478 1128,394 L1128,638 Z"/>
    </svg>

    <div class="brand">
      <span class="brand-mark" aria-hidden="true"></span>
      <div class="brand-text">
        <span class="brand-name">CHL BUREAU</span>
        <span class="brand-tagline">Coastal Hazard &amp; Learning Bureau</span>
      </div>
    </div>

    <div class="person">
      <div class="person-name">Dorian Whitfield</div>
      <div class="person-rule"></div>
      <div class="person-role">Director</div>
    </div>

    <div class="office-contact">
      <div>Ph: 03 9172 4053</div>
      <div>Fx: 03 9172 4055</div>
      <div>dorian.whitfield@chlbureau.com.au</div>
    </div>

    <div class="mobile-contact">
      <div class="mobile"># 0427 391 806</div>
      <div class="website">chlbureau.com.au</div>
    </div>
  </section>
</main>
</body>
</html>
```